Australian new start up company needs a Logo & Web Design

We need a smart, simple logo and web design for a new start up company based in Melbourne Australia called "Merchant Harbour Network". The logo is to be used on all marketing materials. The website is the primary interface of the company.

Our initial phase (launch) will provide a B2B directory service, resources and solutions.
A.) By listing on our site, small businesses can generate sales for their business. Regardless of where they might be located in the world, then can sell to Australian small businesses.
B.)Through our resource centre, small businesses can find practical and up to date resources for their business in pre-start up, start up, growth, maintenance and succession planning or exit stage.
C.)And on our site, we'll offer time and money saving solutions. These solutions can be packaged solutions (ie. Car Branding = including design, print and application onto the vehicle at a discounted price). Customers can also contact us if they want to advertise their business solution.

Eventually, there will be a total of five services inclusive of the directory described above (ie. business classifieds, link to Asian businesses, expos/seminars listing, etc). We hope to see this site grow over the next 18 months. All services will be aimed at servicing small businesses. Individuals through to large businesses located any where in the world can service these small businesses.

We would like to see designs that are professional. They should communicate growth, trust, professionalism and forward thinking.

Target Market(s)

Small Businesses (ie. employ up to 150 employees)

Industry/Entity Type

Business

Requirements
Must have
• We have attached some of the current files that we have designed ourselves. We feel that our material is lacking in appeal, professionalism and consistency. However, it does give a good idea of the requirements needed such as login, directory on the frontpage, etc. The wording is not final, as we are trying to finalise the design first. The logo was simply a placeholder as that definitely needs to be designed.

We want a logo and website that sticks in people's minds, its memorable.

We want a website that is EASY to use and navigate.
Nice to have
• Eventually, there will be a total of five services inclusive of the directory described above (ie. business classifieds, Asian businesses, expos/seminars listing, etc). They are very different types of services. The common thread is that all services will be aimed at servicing small businesses.

The winning design will need to help us to visualize how their design suits our future growth.

```html
<!DOCTYPE html>
<html lang="en">
<head>
<meta charset="utf-8">
<title>Merchant Harbour Network</title>
<link href="https://fonts.googleapis.com/css2?family=Arimo:wght@400;700&family=Roboto+Condensed:wght@400;700&display=swap" rel="stylesheet">
<style>
:root{
  --green:#5cae3c;
  --green-dark:#3f8a26;
  --green-light:#8fd06a;
  --blue:#1a6fae;
  --blue-light:#2e8fd4;
  --teal:#2b9fc4;
  --ink:#2a2a2a;
  --grey:#6b6b6b;
  --row:#e6e6e6;
  --row-edge:#cfcfcf;
  --line:#d9d9d9;
  --hero-top:#6f8291;
  --hero-mid:#a9b7c0;
  --hero-low:#4d6170;
  --white:#ffffff;
}
*{box-sizing:border-box;margin:0;padding:0}
html,body{width:683px;height:1200px;overflow:hidden;background:var(--white)}
body{font-family:"Arimo",Arial,sans-serif;color:var(--ink);position:relative}

/* header */
.site-header{position:absolute;top:0;left:0;width:683px;height:58px}
.brand{position:absolute;left:22px;top:14px;display:flex;align-items:center;gap:8px}
.brand-dot{width:28px;height:28px;border-radius:50%;background:var(--green)}
.brand-name{font-size:15px;font-weight:700;color:var(--green-dark)}
.login{position:absolute;right:22px;top:8px;width:110px;font-size:6px;color:var(--grey)}
.login input{display:block;width:78px;height:9px;border:1px solid var(--line);margin-bottom:3px}
.login .login-row{display:flex;gap:4px;align-items:center}
.login button{width:24px;height:9px;background:var(--green);border:0;color:#fff;font-size:5px}

/* nav */
.main-nav{position:absolute;top:58px;left:0;width:683px;height:18px;border-top:1px solid var(--line);border-bottom:1px solid var(--line);display:flex;padding-left:42px;gap:0}
.main-nav a{font-size:8px;color:var(--grey);text-decoration:none;padding:4px 10px;border-right:1px solid var(--line)}
.main-nav a.current{color:var(--blue);border-bottom:2px solid var(--blue)}

/* hero */
.hero{position:absolute;top:76px;left:0;width:683px;height:290px;background:linear-gradient(180deg,var(--hero-top) 0%,var(--hero-mid) 45%,var(--hero-low) 100%);color:#fff;font-family:"Roboto Condensed",Arial,sans-serif;text-align:center}
.hero-title{margin-top:20px;font-size:21px;font-weight:700;letter-spacing:.2px}
.hero-title small{font-size:13px;font-weight:400}
.hero-points{list-style:none;margin-top:28px;font-size:19px;line-height:30px}
.search{position:absolute;left:22px;top:246px;width:640px;display:flex;align-items:center;gap:10px;font-family:"Arimo",sans-serif}
.search label{font-size:17px;font-weight:700}
.search .field{height:22px;background:var(--green);border:1px solid var(--green-dark);font-size:8px;color:#dff3d2;text-align:left;padding:6px}
.search .what{width:250px}
.search .where{width:80px}
.globe{width:30px;height:30px}

/* tabs */
.tab{position:absolute;height:24px;background:linear-gradient(var(--green-light),var(--green));color:#fff;font-weight:700;font-size:15px;padding:4px 10px;border-radius:3px 3px 0 0}
.tab-browse{top:374px;left:22px;width:208px}
.tab-resource{top:764px;left:455px;width:208px;text-align:center}

/* categories */
.categories{position:absolute;top:406px;left:22px;width:640px;display:flex;gap:48px}
.cat-col{width:181px;list-style:none}
.cat{height:19px;margin-bottom:3px;background:linear-gradient(#f2f2f2,var(--row));border:1px solid var(--row-edge);font-size:7.5px;font-weight:700;padding:4px 5px;position:relative}
.cat::after{content:"";position:absolute;right:3px;top:6px;border-left:4px solid transparent;border-right:4px solid transparent;border-top:5px solid var(--blue)}
.cat.open{background:var(--blue-light);color:#fff;border-color:var(--blue)}
.cat.open::after{border-top-color:#fff}
.sub{list-style:none;border:1px solid var(--row-edge);border-top:0;padding:2px 6px 4px;margin:-3px 0 3px}
.sub li{font-size:6px;color:var(--grey);line-height:9.4px}

/* packages */
.packages{position:absolute;top:798px;left:22px;width:640px;display:flex;gap:12px}
.package{width:151px;height:200px;border:1px solid var(--line);position:relative}
.package h3{height:58px;background:var(--teal);border-bottom:8px solid var(--blue);color:#fff;font-size:14px;line-height:17px;padding:6px 8px;font-weight:700;background:linear-gradient(var(--white) 0 0) top/100% 0 no-repeat,var(--white);color:var(--ink);border-bottom:0}
.package .band{height:8px;background:var(--teal)}
.package ul{list-style:none;margin:6px 8px 0;border:1px solid var(--line)}
.package li{font-size:6px;color:#fff;background:var(--blue-light);padding:2px 4px;border-bottom:1px solid #fff}
.go{position:absolute;right:0;bottom:0;width:26px;height:15px;background:var(--green);color:#fff;font-size:8px;font-weight:700;text-align:center;line-height:15px}
.package-foot{position:absolute;left:0;right:0;bottom:0;height:15px;background:var(--teal)}

/* bottom categories */
.more-cats{position:absolute;top:1036px;left:22px;width:640px;display:grid;grid-template-columns:repeat(3,181px);column-gap:48px;row-gap:14px}
.more-cats span{height:18px;background:var(--blue-light);color:#fff;font-size:8px;font-weight:700;padding:4px 6px;position:relative}
.more-cats span::after{content:"";position:absolute;right:5px;top:6px;border-left:4px solid transparent;border-right:4px solid transparent;border-top:5px solid #fff}

/* footer */
.site-footer{position:absolute;top:1140px;left:0;width:683px;height:60px;border-top:1px solid var(--line);font-size:7px;color:var(--grey)}
.foot-links{position:absolute;left:42px;top:10px;display:grid;grid-template-columns:repeat(4,70px);row-gap:8px}
.contact{position:absolute;right:42px;top:10px;display:flex;gap:4px;align-items:center}
.contact i{display:block;width:13px;height:13px;background:var(--blue);border-radius:2px}
.copyright{position:absolute;left:0;right:0;bottom:8px;text-align:center;font-size:5px}
</style>
</head>
<body>

<header class="site-header">
  <div class="brand"><span class="brand-dot"></span><span class="brand-name">Merchant Harbour Network</span></div>
  <form class="login">
    <input type="text" aria-label="Username">
    <div class="login-row"><input type="password" aria-label="Password" style="width:60px;margin:0"><button type="button">Login</button></div>
    <div style="margin-top:3px">Forgot your password?</div>
  </form>
</header>

<nav class="main-nav">
  <a class="current">Home</a><a>About Us</a><a>Online Directory</a><a>Features</a><a>Pricing</a><a>Order</a><a>Support</a>
</nav>

<section class="hero" role="img" aria-label="Calm harbour water under an overcast sky">
  <h1 class="hero-title"><small>Online directory,</small> dedicated to servicing Australian Small Businesses</h1>
  <ul class="hero-points">
    <li>Advertise for as little as $2/month</li>
    <li>Generate sales, increase brand awareness</li>
    <li>Limited time business offers</li>
    <li>Small Business resource centre</li>
  </ul>
  <div class="search">
    <label>I need</label>
    <div class="field what">enter your search keyword...</div>
    <label style="margin-left:50px">Located in</label>
    <div class="field where">enter suburb</div>
    <svg class="globe" viewBox="0 0 30 30"><circle cx="15" cy="15" r="13" fill="#4a9ad4" stroke="#fff" stroke-width="1.5"/><ellipse cx="15" cy="15" rx="6" ry="13" fill="none" stroke="#fff" stroke-width="1"/><line x1="2" y1="15" x2="28" y2="15" stroke="#fff"/><path d="M5 8h20M5 22h20" stroke="#fff" stroke-width=".8"/></svg>
  </div>
</section>

<div class="tab tab-browse">Browse by Categories</div>

<section class="categories">
  <ul class="cat-col">
    <li class="cat">Accounting</li>
    <li class="cat open">Artwork Design</li>
    <li><ul class="sub">
      <li>Banner</li><li>Blog</li><li>Brochure</li><li>Electronic Stationery</li><li>Template</li><li>Social Page</li><li>Flyer</li><li>Logo</li><li>Powerpoint</li><li>Restaurant Menu</li><li>Stationery</li><li>Sticker</li><li>T-Shirt</li><li>Social Banner</li><li>Vehicle Signage</li><li>Website Design</li>
    </ul></li>
    <li class="cat">Banking &amp; Finance</li>
    <li class="cat">Category</li>
    <li class="cat">Category</li>
    <li class="cat">Category</li>
    <li class="cat">Category</li>
  </ul>
  <ul class="cat-col">
    <li class="cat">Bookkeeping</li>
    <li class="cat">Capital Raising</li>
    <li class="cat">Cleaning Services &amp; Suppliers</li>
    <li class="cat">Coaching/Training</li>
    <li class="cat">Courier Service</li>
    <li class="cat">Equipment Hire</li>
    <li class="cat">Event planning &amp; Coordination</li>
    <li class="cat">Facilities</li>
    <li class="cat">Fitness</li>
    <li class="cat">Information Technology</li>
    <li class="cat">Insurance</li>
    <li class="cat">Legal Advice</li>
    <li class="cat">Manufacturing</li>
    <li class="cat">Marketing &amp; Public Relations</li>
    <li class="cat">Payroll Services</li>
    <li class="cat">Category</li>
    <li class="cat">Category</li>
  </ul>
  <ul class="cat-col">
    <li class="cat">Photography/Videography</li>
    <li class="cat">Printing</li>
    <li class="cat">Promotional Materials</li>
    <li class="cat">Recruitment</li>
    <li class="cat">Sales</li>
    <li class="cat">Sewing &amp; Tailoring</li>
    <li class="cat">Shop Fit Outs &amp; Equipment</li>
    <li class="cat">Signage</li>
    <li class="cat">Stationery</li>
    <li class="cat">Superannuation</li>
    <li class="cat">Taxation</li>
    <li class="cat">Translation Service</li>
    <li class="cat">Travel Service</li>
    <li class="cat">Uniforms/Corporate Wear</li>
    <li class="cat">Repair &amp; Maintenance</li>
    <li class="cat">Virtual Assistants</li>
  </ul>
</section>

<div class="tab tab-resource">Resource Centre</div>

<section class="packages">
  <article class="package"><div class="band"></div><h3>Start-Up Package $2000</h3>
    <ul><li>Logo Design</li><li>Website Design</li><li>Stationery</li><li>Directory Listing</li></ul>
    <div class="package-foot"></div><span class="go">go</span></article>
  <article class="package"><div class="band"></div><h3>Biz Growth Package $1000</h3>
    <ul><li>Logo Design</li><li>Website Design</li><li>Directory Listing</li></ul>
    <div class="package-foot"></div><span class="go">go</span></article>
  <article class="package"><div class="band"></div><h3>Biz Coaching $2500</h3>
    <ul><li>10 hours of</li><li>Business Coaching</li><li>Directory Listing</li></ul>
    <div class="package-foot"></div><span class="go">go</span></article>
  <article class="package"><div class="band"></div><h3>Vehicle Advertising $xx</h3>
    <ul><li>Artwork Printing</li><li>Vehicle Placement</li><li>Directory Listing</li></ul>
    <div class="package-foot"></div><span class="go">go</span></article>
</section>

<section class="more-cats">
  <span>Category1</span><span>Category4</span><span>Category7</span>
  <span>Category2</span><span>Category5</span><span>Category8</span>
  <span>Category3</span><span>Category6</span><span>Category9</span>
</section>

<footer class="site-footer">
  <div class="foot-links">
    <span>How it works</span><span>Login</span><span>Resource Centre</span><span>Terms &amp; Conditions</span>
    <span>Post an Ad</span><span>Contact Us</span><span>Add Link</span><span>Privacy Policy</span>
  </div>
  <div class="contact"><span>Contact Us</span><i></i><i></i><i></i></div>
  <p class="copyright">© Merchant Harbour Network 2013. All rights reserved. Use of this site is subject to our Terms and Privacy Policy.</p>
</footer>

</body>
</html>
```